No Credit Score TQ and KSV

I'm looking for a banner to display on emails as well as facebook. The facebook banner would need to be square and the other size is 728 x 90. We are a mortgage company that does mostly Military home loans. We would like to start out with just this banner, then do about 20 others once we find the right designer. I need something simple but that stands out. Our company website is www.harborpeakloans.com. The text for this will be ( Ask about our "No Credit Score" program for KSV and TQ)

```html
<!DOCTYPE html>
<html lang="en">
<head>
<meta charset="utf-8">
<title>No Credit Score Program Banners</title>
<link href="https://fonts.googleapis.com/css2?family=Exo+2:wght@500;800&family=Open+Sans:wght@500&display=swap" rel="stylesheet">
<style>
  :root {
    --stage: #121212;
    --stage-glow: #1c1c1c;
    --navy-dark: #141a4c;
    --navy: #222a70;
    --periwinkle: #7276e6;
    --accent-red: #e0141c;
    --white: #ffffff;
    --label-grey: #bdbdbd;
    --flag-red: #c8202c;
    --flag-white: #f2eeee;
    --house-cream: #d9cdb3;
    --sky: #e8e6e4;
    --foliage: #6c7550;
  }
  html, body {
    margin: 0;
    padding: 0;
    overflow: hidden;
  }
  body {
    width: 1200px;
    height: 800px;
    background: radial-gradient(ellipse at 50% 40%, var(--stage-glow), var(--stage) 70%);
    position: relative;
    font-family: "Exo 2", sans-serif;
  }
  .variant-number {
    position: absolute;
    left: 96px;
    width: 40px;
    text-align: center;
    font-family: "Exo 2", sans-serif;
    font-weight: 800;
    font-size: 40px;
    color: var(--label-grey);
    line-height: 1;
  }
  .banner {
    position: absolute;
    left: 203px;
    width: 800px;
    height: 99px;
    overflow: hidden;
    background: linear-gradient(90deg, var(--navy) 0%, var(--navy-dark) 60%);
  }
  .banner-photo {
    position: absolute;
    inset: 0;
    width: 800px;
    height: 99px;
  }
  .ask-about {
    position: absolute;
    left: 13px;
    top: 11px;
    font-weight: 500;
    font-size: 24px;
    line-height: 25.5px;
    color: var(--periwinkle);
    margin: 0;
  }
  .chevron {
    position: absolute;
    left: 97px;
    top: 19px;
    width: 28px;
    height: 60px;
  }
  .headline {
    position: absolute;
    left: 130px;
    top: 20px;
    margin: 0;
    color: var(--white);
    font-weight: 800;
    font-size: 24px;
    line-height: 26px;
    letter-spacing: 0.2px;
  }
  .headline .audience {
    font-family: "Open Sans", sans-serif;
    font-weight: 500;
    font-size: 15.5px;
    letter-spacing: 0;
  }
  .underline {
    position: absolute;
    left: 130px;
    top: 75px;
    width: 248px;
    height: 2px;
    background: var(--accent-red);
  }
</style>
</head>
<body>

  <div class="variant-number" style="top:176px">1</div>
  <section class="banner" style="top:138px">
    <svg class="banner-photo" viewBox="0 0 800 99" role="img" aria-label="Waving American flag blending into a photo of a cream two-storey house">
      <defs>
        <linearGradient id="scene-one" x1="0" x2="1" y1="0" y2="0">
          <stop offset="0" stop-color="#1a2260" stop-opacity="0"/>
          <stop offset="0.12" stop-color="#2b3a9a"/>
          <stop offset="0.3" stop-color="var(--flag-red)"/>
          <stop offset="0.42" stop-color="var(--flag-white)"/>
          <stop offset="0.6" stop-color="var(--house-cream)"/>
          <stop offset="1" stop-color="var(--sky)"/>
        </linearGradient>
      </defs>
      <rect x="440" y="0" width="360" height="99" fill="url(#scene-one)"/>
    </svg>
    <p class="ask-about">ASK<br>ABOUT<br>OUR</p>
    <svg class="chevron" viewBox="0 0 28 60"><polygon points="0,0 10,0 28,30 10,60 0,60 16,30" fill="var(--accent-red)"/></svg>
    <h2 class="headline">NO CREDIT SCORE<br>PROGRAM <span class="audience">FOR KSV AND TQ</span></h2>
    <div class="underline"></div>
  </section>

  <div class="variant-number" style="top:312px">2</div>
  <section class="banner" style="top:280px">
    <svg class="banner-photo" viewBox="0 0 800 99" role="img" aria-label="Photo of a cream two-storey house beside a waving American flag">
      <defs>
        <linearGradient id="scene-two" x1="0" x2="1" y1="0" y2="0">
          <stop offset="0" stop-color="var(--house-cream)"/>
          <stop offset="0.45" stop-color="var(--sky)"/>
          <stop offset="0.55" stop-color="#3548a8"/>
          <stop offset="0.7" stop-color="var(--flag-red)"/>
          <stop offset="0.85" stop-color="var(--flag-white)"/>
          <stop offset="1" stop-color="var(--flag-red)"/>
        </linearGradient>
      </defs>
      <polygon points="458,0 800,0 800,99 374,99" fill="url(#scene-two)"/>
    </svg>
    <p class="ask-about">ASK<br>ABOUT<br>OUR</p>
    <svg class="chevron" viewBox="0 0 28 60"><polygon points="0,0 10,0 28,30 10,60 0,60 16,30" fill="var(--accent-red)"/></svg>
    <h2 class="headline">NO CREDIT SCORE<br>PROGRAM <span class="audience">FOR KSV AND TQ</span></h2>
    <div class="underline"></div>
  </section>

  <div class="variant-number" style="top:459px">3</div>
  <section class="banner" style="top:422px">
    <svg class="banner-photo" viewBox="0 0 800 99" role="img" aria-label="Photo of a cream house among trees with an American flag on the right">
      <defs>
        <linearGradient id="scene-three" x1="0" x2="1" y1="0" y2="0">
          <stop offset="0" stop-color="var(--foliage)"/>
          <stop offset="0.15" stop-color="var(--house-cream)"/>
          <stop offset="0.55" stop-color="var(--sky)"/>
          <stop offset="0.68" stop-color="#3548a8"/>
          <stop offset="0.82" stop-color="var(--flag-red)"/>
          <stop offset="1" stop-color="var(--flag-white)"/>
        </linearGradient>
      </defs>
      <polygon points="458,0 800,0 800,99 374,99" fill="url(#scene-three)"/>
    </svg>
    <p class="ask-about">ASK<br>ABOUT<br>OUR</p>
    <svg class="chevron" viewBox="0 0 28 60"><polygon points="0,0 10,0 28,30 10,60 0,60 16,30" fill="var(--accent-red)"/></svg>
    <h2 class="headline">NO CREDIT SCORE<br>PROGRAM <span class="audience">FOR KSV AND TQ</span></h2>
    <div class="underline"></div>
  </section>

  <div class="variant-number" style="top:592px">4</div>
  <section class="banner" style="top:564px">
    <svg class="banner-photo" viewBox="0 0 800 99" role="img" aria-label="Photo of a soldier in uniform walking toward a grey house with an American flag in the corner">
      <defs>
        <linearGradient id="scene-four" x1="0" x2="1" y1="0" y2="0">
          <stop offset="0" stop-color="#f4f1ea"/>
          <stop offset="0.15" stop-color="#6e6a62"/>
          <stop offset="0.45" stop-color="#8a8676"/>
          <stop offset="0.65" stop-color="var(--flag-red)"/>
          <stop offset="0.8" stop-color="var(--flag-white)"/>
          <stop offset="1" stop-color="#3a4a8a"/>
        </linearGradient>
      </defs>
      <polygon points="458,0 800,0 800,99 374,99" fill="url(#scene-four)"/>
    </svg>
    <p class="ask-about">ASK<br>ABOUT<br>OUR</p>
    <svg class="chevron" viewBox="0 0 28 60"><polygon points="0,0 10,0 28,30 10,60 0,60 16,30" fill="var(--accent-red)"/></svg>
    <h2 class="headline">NO CREDIT SCORE<br>PROGRAM <span class="audience">FOR KSV AND TQ</span></h2>
    <div class="underline"></div>
  </section>

</body>
</html>
```